Memoir author looking for book cover design

Title:
"Rain, Rust and Return"

Subtitle:
"A Season Spent Chasing Our Father Across the Coastline"

My book is about the 18-month-long search and grieving process after my husband went missing from a hiking accident.
See "notesbeyondthequietharbor.example" for background

(An "ampersand" may look best, but I'm unable to enter it in this format)

Reason: Having difficulty finishing up, in part due to time difference. Don't want designers to have to work in the middle of the night!

```html
<!DOCTYPE html>
<html lang="en">
<head>
<meta charset="utf-8">
<title>Rain, Rust and Return — Book Cover</title>
<link rel="stylesheet" href="https://fonts.googleapis.com/css2?family=Anton&family=Montserrat:wght@400&display=swap">
<style>
  :root {
    --paper: #f3f3f1;
    --paper-edge: #e6e6e3;
    --ink: #1b1616;
    --shadow: #050505;
    --sky: #b4daf3;
    --ridge: #6f93bd;
    --forest-light: #4f6e4a;
    --forest-dark: #2c4329;
    --rock: #8b817c;
  }
  html, body {
    margin: 0;
    padding: 0;
    width: 821px;
    height: 1200px;
    overflow: hidden;
    background: var(--paper);
  }
  .cover {
    position: relative;
    width: 821px;
    height: 1200px;
    background: radial-gradient(ellipse at center, var(--paper) 55%, var(--paper-edge) 100%);
    overflow: hidden;
  }
  .title-art {
    position: absolute;
    left: 0;
    top: 0;
    width: 821px;
    height: 870px;
  }
  .title-word {
    font-family: 'Anton', sans-serif;
  }
  .subtitle {
    position: absolute;
    left: 0;
    right: 0;
    top: 887px;
    margin: 0;
    text-align: center;
    font-family: 'Montserrat', sans-serif;
    font-weight: 400;
    font-size: 31px;
    line-height: 40px;
    color: var(--ink);
    text-transform: uppercase;
    letter-spacing: 0.2px;
  }
  .author {
    position: absolute;
    left: 0;
    right: 0;
    top: 1084px;
    margin: 0;
    text-align: center;
    font-family: 'Montserrat', sans-serif;
    font-weight: 400;
    font-size: 64px;
    line-height: 72px;
    letter-spacing: 18px;
    padding-left: 18px;
    color: var(--ink);
  }
</style>
</head>
<body>
<main class="cover">
  <svg class="title-art" viewBox="0 0 821 870" role="img"
       aria-label="Title lettering RAIN, RUST & RETURN filled with a photograph of a mountain ridge, pine forest and a hiker on a rocky slope">
    <defs>
      <linearGradient id="landscape-fill" gradientUnits="userSpaceOnUse" x1="0" y1="94" x2="0" y2="840">
        <stop offset="0" stop-color="var(--sky)"/>
        <stop offset="0.2" stop-color="var(--sky)"/>
        <stop offset="0.3" stop-color="var(--ridge)"/>
        <stop offset="0.5" stop-color="var(--forest-light)"/>
        <stop offset="0.78" stop-color="var(--forest-dark)"/>
        <stop offset="1" stop-color="var(--rock)"/>
      </linearGradient>
    </defs>
    <g class="title-shadow" fill="var(--shadow)" transform="translate(3 6)">
      <text class="title-word" x="86" y="376" font-size="327" textLength="638" lengthAdjust="spacingAndGlyphs">RAIN</text>
      <text class="title-word" x="86" y="664" font-size="327" textLength="638" lengthAdjust="spacingAndGlyphs">RUST</text>
      <text class="title-word" x="86" y="840" font-size="192" textLength="638" lengthAdjust="spacingAndGlyphs">&amp; RETURN</text>
    </g>
    <g class="title-fill" fill="url(#landscape-fill)">
      <text class="title-word" x="86" y="376" font-size="327" textLength="638" lengthAdjust="spacingAndGlyphs">RAIN</text>
      <text class="title-word" x="86" y="664" font-size="327" textLength="638" lengthAdjust="spacingAndGlyphs">RUST</text>
      <text class="title-word" x="86" y="840" font-size="192" textLength="638" lengthAdjust="spacingAndGlyphs">&amp; RETURN</text>
    </g>
  </svg>

  <p class="subtitle">A Season Spent Chasing Our Father<br>Across the Coastline</p>

  <p class="author">AUTHOR NAME</p>
</main>
</body>
</html>
```